Etiketten-Design für Kräuterbonbon-Metalldose
Marlene Vosk hat sehr viel Talent. Das Design ist absolut kreativ.
Zielgruppe
Unsere Firma VelbraCor verkauft verschiedene Sorten Kräuterbonbons.
Wir brauchen ein Etikett, dass auf eine Metall-Dose (Durchmesser 10 cam, Höhe ca. 3 cm) geklebt wird.
Zielgruppe: jung-alt
Aufgabenstellung
Der Name unserer Kräuterbonbons ist Pfeffling.
Wir möchten, dass unsere Kunden, wenn sie das Etikett sehen einen Bezug zur Schweiz herstellen können.
Wir verwenden für unsere Bonbons unterschiedliche Kräuter für verschiedene Anwendungen:
Konkret sind erstmal 4 Dosen geplant:
-Kräutermischung aus 16 Kräuter gegen Husten
-Salbei gegen Halsschmerzen
-Anis gegen Magenschmerzen
-Zitrone/Ingwer für die Nerven
Vorderseite: Produktbeschreibung
Rückseite: unsere Herstellerangaben
Größenangaben der Dose: Durchmesser 10 cm, Höhe ca. 3 cm
Im Anhang habe ich Ihnen noch weitere/ genauere Informationen zur Verfügung bereitgestellt!

```html
<!DOCTYPE html>
<html lang="de">
<head>
<meta charset="utf-8">
<title>Pfeffling – Kräuterbonbon Dosenetikett</title>
<link rel="stylesheet" href="https://fonts.googleapis.com/css2?family=Open+Sans:wght@400;600;700&family=PT+Sans+Narrow:wght@700&display=swap">
<style>
  :root {
    --bg: #ffffff;
    --rim: #e2e4e3;
    --rim-edge: #cdd0cf;
    --green: #8cbd48;
    --green-deep: #7eae38;
    --green-light: #a2cf5a;
    --text-green: #86b53e;
    --paper: #eaecea;
    --white: #ffffff;
  }
  * { margin: 0; padding: 0; box-sizing: border-box; }
  html, body { width: 1200px; height: 600px; overflow: hidden; background: var(--bg); }
  .canvas {
    width: 1200px; height: 600px;
    display: flex; align-items: center; justify-content: space-around;
    padding: 0 40px;
  }
  .label { width: 480px; height: 480px; display: block; }
  .title-narrow { font-family: "PT Sans Narrow", "Arial Narrow", sans-serif; font-weight: 700; }
  .body-sans { font-family: "Open Sans", Arial, sans-serif; }
</style>
</head>
<body>
<main class="canvas">

  <!-- Vorderseite -->
  <svg class="label label-front" viewBox="0 0 480 480" aria-label="Vorderseite Etikett Pfeffling">
    <defs>
      <path id="arc-top" d="M 62 240 A 178 178 0 0 1 418 240"/>
      <path id="arc-bottom" d="M 50 240 A 190 190 0 0 0 430 240"/>
      <linearGradient id="herb-fill" x1="0" y1="0" x2="0" y2="1">
        <stop offset="0" stop-color="#6fae4a"/>
        <stop offset="1" stop-color="#2f7a34"/>
      </linearGradient>
    </defs>
    <circle class="rim" cx="240" cy="240" r="238" fill="var(--rim)" stroke="var(--rim-edge)" stroke-width="2"/>
    <circle class="ring" cx="240" cy="240" r="215" fill="var(--green)"/>
    <circle class="field" cx="240" cy="240" r="160" fill="var(--paper)"/>

    <text class="title-narrow brand-name" font-size="36" fill="var(--white)" letter-spacing="1">
      <textPath href="#arc-top" startOffset="50%" text-anchor="middle">Pfeffling</textPath>
    </text>
    <rect class="ornament" role="img" aria-label="Zweig-Ornament" x="98" y="118" width="34" height="22" rx="10" fill="var(--green-light)" transform="rotate(-35 115 129)"/>
    <rect class="ornament" role="img" aria-label="Zweig-Ornament" x="348" y="118" width="34" height="22" rx="10" fill="var(--green-light)" transform="rotate(35 365 129)"/>

    <text class="body-sans tagline" font-size="17" font-weight="700" fill="var(--white)" letter-spacing="2">
      <textPath href="#arc-bottom" startOffset="50%" text-anchor="middle">Schweizer Kräuterbonbon</textPath>
    </text>

    <rect class="tab tab-weight" x="28" y="212" width="74" height="54" rx="27" fill="var(--green)"/>
    <text class="title-narrow" x="62" y="250" font-size="28" fill="var(--white)" text-anchor="middle">125G</text>
    <rect class="tab tab-count" x="376" y="212" width="82" height="54" rx="27" fill="var(--green)"/>
    <text class="title-narrow" x="419" y="250" fill="var(--white)" text-anchor="middle"><tspan font-size="28">16</tspan><tspan font-size="14" dx="3">pieces</tspan></text>

    <ellipse class="leaf-icon" role="img" aria-label="Kräuterzweig-Symbol" cx="240" cy="112" rx="14" ry="32" fill="var(--text-green)"/>

    <g class="title-narrow product-name" fill="var(--text-green)" text-anchor="middle" font-size="35">
      <text x="240" y="196">Kräutermischung</text>
      <text x="240" y="232">aus 16 Kräuter</text>
      <text x="240" y="268">gegen Husten</text>
    </g>

    <path class="herb-illustration" role="img" aria-label="Illustration eines Kräuterbündels" d="M 186 390 C 160 340 190 290 240 280 C 290 290 318 340 294 390 Z" fill="url(#herb-fill)"/>
  </svg>

  <!-- Rückseite -->
  <svg class="label label-back" viewBox="0 0 480 480" aria-label="Rückseite Etikett Nährwerte">
    <defs>
      <linearGradient id="disc-fill" x1="0" y1="0" x2="1" y2="1">
        <stop offset="0" stop-color="var(--green-light)"/>
        <stop offset="1" stop-color="var(--green-deep)"/>
      </linearGradient>
    </defs>
    <circle class="rim" cx="240" cy="240" r="238" fill="var(--rim)" stroke="var(--rim-edge)" stroke-width="2"/>
    <circle class="disc" cx="240" cy="240" r="212" fill="url(#disc-fill)"/>

    <ellipse class="leaf-icon" role="img" aria-label="Kräuterzweig-Symbol" cx="240" cy="82" rx="13" ry="28" fill="var(--paper)"/>

    <text class="body-sans heading" x="240" y="138" font-size="17" font-weight="700" fill="var(--paper)" text-anchor="middle">Unzubereitet für 100 Gramm</text>

    <g class="body-sans badges" text-anchor="middle">
      <g transform="translate(123 192)">
        <circle r="29" fill="var(--paper)"/><circle r="25" fill="none" stroke="var(--green)" stroke-width="1.5"/>
        <text y="-6" font-size="7.5" fill="var(--text-green)">Energie</text>
        <text y="8" font-size="9" font-weight="700" fill="var(--text-green)">400 Kcal</text>
      </g>
      <g transform="translate(240 192)">
        <circle r="29" fill="var(--paper)"/><circle r="25" fill="none" stroke="var(--green)" stroke-width="1.5"/>
        <text y="-6" font-size="7.5" fill="var(--text-green)">Energie</text>
        <text y="8" font-size="9" font-weight="700" fill="var(--text-green)">1670 kj</text>
      </g>
      <g transform="translate(357 192)">
        <circle r="29" fill="var(--paper)"/><circle r="25" fill="none" stroke="var(--green)" stroke-width="1.5"/>
        <text y="-6" font-size="7.5" fill="var(--text-green)">Fett</text>
        <text y="8" font-size="9" font-weight="700" fill="var(--text-green)">0 g</text>
      </g>
    </g>

    <rect class="nutrition-box" x="94" y="246" width="292" height="108" rx="14" fill="none" stroke="var(--paper)" stroke-width="1.6"/>
    <g class="body-sans nutrition-table" font-size="10.5" fill="var(--paper)">
      <text x="108" y="266">Energie</text><text x="280" y="266" font-weight="600">400 Kcal  / 1670 kj</text>
      <text x="108" y="279">Fett</text><text x="280" y="279" font-weight="600">0 g</text>
      <text x="108" y="292">davon gesättigte Fettsäuren</text><text x="280" y="292" font-weight="600">0 g</text>
      <text x="108" y="305">kohlenhydrate</text><text x="280" y="305" font-weight="600">98 g</text>
      <text x="108" y="318">davon Zucker</text><text x="280" y="318" font-weight="600">76 g</text>
      <text x="108" y="331">Eiweiß</text><text x="280" y="331" font-weight="600">0 g</text>
      <text x="108" y="344">Salz</text><text x="280" y="344" font-weight="600">0 g</text>
    </g>

    <rect class="ornament" role="img" aria-label="Zweig-Ornament" x="180" y="404" width="120" height="20" rx="10" fill="var(--green-light)"/>
  </svg>

</main>
</body>
</html>
```